Lotzy Template Design in Baby Category

We are a maternity/baby store on Lotzy in need of a store front design template (Store front, listing and detail page page) that is accustom to our category, is user friendly, easy to read and navigate and mobile friendly.

The design should be reflecting a motherhood warm feeling with a modern look.

Please don't hesitate to inquire, if you need any clarification.

Thank you

Baby

3 page

```html
<!DOCTYPE html>
<html lang="en">
<head>
<meta charset="utf-8">
<title>Little Bloom – Lotzy Store Front</title>
<link rel="stylesheet" href="https://fonts.googleapis.com/css2?family=Open+Sans:wght@400;600;700;800&display=swap">
<style>
:root{
  --purple:#7b4fa6;
  --purple-dark:#5e3a84;
  --nav:#2f2f33;
  --nav-dark:#1e1e21;
  --grey-bg:#f1f1f1;
  --grey-line:#dcdcdc;
  --text:#555;
  --text-light:#999;
  --red:#d63a2f;
  --white:#fff;
}
*{box-sizing:border-box;margin:0;padding:0}
html,body{width:831px;height:1200px;overflow:hidden}
body{font-family:"Open Sans",Arial,sans-serif;color:var(--text);background:var(--white);position:relative}
.topbar{position:absolute;top:0;left:470px;right:0;height:22px;background:var(--purple);display:flex;align-items:center;gap:10px;padding-left:40px;font-size:7px;font-weight:700;color:var(--white);letter-spacing:.3px}
.topbar span.sep{opacity:.6}
.header{position:absolute;top:22px;left:135px;width:560px;height:76px}
.brand{position:absolute;left:8px;top:12px;display:flex;align-items:center;gap:8px}
.brand-mark{width:24px;height:24px;border-radius:50%;background:var(--purple)}
.brand-name{font-family:"Open Sans",Arial,sans-serif;font-weight:700;font-size:20px;color:var(--purple-dark);line-height:1}
.brand-tag{position:absolute;left:40px;top:42px;font-size:7px;color:var(--text-light);letter-spacing:.5px}
.contact{position:absolute;right:0;top:8px;font-size:8px;color:var(--text)}
.contact li{list-style:none;display:flex;align-items:center;gap:6px;height:18px}
.contact svg{width:12px;height:12px}
.nav{position:absolute;top:98px;left:135px;width:560px;height:24px;background:var(--nav);display:flex;align-items:center;font-size:7.5px;font-weight:700;color:var(--white)}
.nav .home{width:30px;height:24px;background:var(--nav-dark);display:flex;align-items:center;justify-content:center}
.nav a{padding:0 11px;color:var(--white);text-decoration:none}
.search{margin-left:auto;margin-right:6px;width:120px;height:15px;background:var(--white);border-radius:2px;font-weight:400;color:var(--text-light);font-size:7px;display:flex;align-items:center;justify-content:space-between;padding:0 5px}
.sidebar{position:absolute;top:130px;left:140px;width:128px}
.side-head{background:var(--purple);color:var(--white);font-size:8px;font-weight:700;height:20px;display:flex;align-items:center;padding-left:8px;border-radius:3px 3px 0 0}
.cat-list{background:var(--grey-bg);border:1px solid var(--grey-line);border-top:none;padding:4px 0}
.cat-list li{list-style:none;font-size:7.5px;height:22px;display:flex;align-items:center;padding-left:10px;border-bottom:1px solid var(--grey-line)}
.cat-list li:last-child{border-bottom:none}
.cat-list li::before{content:"›";color:var(--purple);margin-right:5px;font-weight:700}
.pay{margin-top:14px}
.pay-body{background:var(--grey-bg);border:1px solid var(--grey-line);border-top:none;height:78px;display:flex;flex-wrap:wrap;gap:6px;padding:12px 10px;align-content:center;justify-content:center}
.pay-body .badge{width:46px;height:18px;border-radius:3px;background:#c9c9c9}
.pay-body .badge.alt{background:#b6a6c8}
.main{position:absolute;top:130px;left:285px;width:410px}
.toolbar{height:20px;background:var(--grey-bg);border:1px solid var(--grey-line);display:flex;align-items:center;padding:0 8px;font-size:6.5px;font-weight:700;gap:12px}
.toolbar .view{color:var(--purple)}
.toolbar .sort{margin-left:auto;background:var(--white);border:1px solid var(--grey-line);padding:1px 14px 1px 4px;font-weight:400}
.grid{display:grid;grid-template-columns:repeat(3,1fr);gap:10px;margin-top:10px}
.card{height:186px;border:1px solid var(--grey-line);background:var(--white);padding:6px;display:flex;flex-direction:column}
.product-img{height:78px;display:flex;justify-content:center;align-items:flex-end}
.product-img .jar{width:56px;height:64px;border-radius:6px;background:linear-gradient(#f4e9a8,#e7c45c)}
.product-img .bottle{width:30px;height:72px;border-radius:6px 6px 3px 3px;background:linear-gradient(#6b3e2a,#3e2217)}
.product-img .wash{width:34px;height:74px;border-radius:8px 8px 3px 3px;background:linear-gradient(#f6d0a6,#d9925a)}
.title{font-size:6.5px;font-weight:700;color:var(--purple);line-height:1.35;margin-top:6px;height:18px}
.price{display:flex;justify-content:space-between;font-size:6.5px;margin-top:5px;line-height:1.45}
.buy{color:var(--red);font-weight:800}
.buy b{color:var(--purple)}
.old{text-decoration:line-through;color:var(--text-light)}
.meta{color:var(--text-light)}
.now{color:var(--red);font-weight:700}
.btn{margin:auto auto 2px;background:var(--purple);color:var(--white);font-size:6.5px;font-weight:700;padding:4px 12px;border-radius:2px}
.pager{position:absolute;top:1138px;left:285px;width:410px;height:18px;background:var(--nav);display:flex;align-items:center;justify-content:center;gap:7px;font-size:6.5px;font-weight:700;color:var(--white)}
.pager .on{color:#c7a6ea}
.footer{position:absolute;top:1180px;left:0;width:831px;text-align:center;font-size:6.5px;color:var(--text-light)}
</style>
</head>
<body>
<div class="topbar"><span>SALE</span><span class="sep">|</span><span>AUCTIONS</span><span class="sep">|</span><span>ENDING SOON</span><span class="sep">|</span><span>NEWLY LISTED</span></div>

<header class="header">
  <div class="brand"><span class="brand-mark"></span><span class="brand-name">Little Bloom</span></div>
  <div class="brand-tag">MATERNITY &amp; BABY STORE</div>
  <ul class="contact">
    <li><svg viewBox="0 0 12 12"><circle cx="6" cy="6" r="6" fill="#7b4fa6"/><path d="M4 3.2l1 1.4-.6.8a4 4 0 0 0 2.2 2.2l.8-.6 1.4 1-.7 1C6 9 3 6 3.2 3.9z" fill="#fff"/></svg>(555) 014-2280</li>
    <li><svg viewBox="0 0 12 12"><circle cx="6" cy="6" r="6" fill="#7b4fa6"/><rect x="3" y="4" width="6" height="4" fill="none" stroke="#fff" stroke-width=".8"/><path d="M3 4l3 2.2L9 4" fill="none" stroke="#fff" stroke-width=".8"/></svg>hello@littlebloom.shop</li>
    <li><svg viewBox="0 0 12 12"><circle cx="6" cy="6" r="6" fill="#7b4fa6"/><circle cx="6" cy="6" r="3" fill="none" stroke="#fff" stroke-width=".8"/><path d="M3 6h6M6 3v6" stroke="#fff" stroke-width=".6"/></svg>www.littlebloom.shop</li>
  </ul>
</header>

<nav class="nav">
  <span class="home"><svg width="11" height="10" viewBox="0 0 11 10"><path d="M5.5 0L0 5h1.5v5h3V7h2v3h3V5H11z" fill="#fff"/></svg></span>
  <a>ABOUT US</a><a>PAYMENT</a><a>SHIPPING</a><a>TERMS</a><a>CONTACT US</a><a>OUR STORE</a>
  <div class="search">Search store...<svg width="8" height="8" viewBox="0 0 8 8"><circle cx="3.2" cy="3.2" r="2.4" fill="none" stroke="#7b4fa6" stroke-width="1"/><path d="M5 5l2.5 2.5" stroke="#7b4fa6" stroke-width="1.2"/></svg></div>
</nav>

<aside class="sidebar">
  <div class="side-head">CATEGORIES</div>
  <ul class="cat-list">
    <li>Baby Care</li><li>Nutrition</li><li>Supplements</li><li>Clothings</li><li>Baby Care</li><li>Supplements</li><li>Clothings</li><li>Baby Care</li><li>Supplements</li><li>Nutrition</li><li>Baby Care</li><li>Supplements</li><li>Nutrition</li><li>Others</li>
  </ul>
  <div class="pay">
    <div class="side-head">PAYMENT</div>
    <div class="pay-body">
      <span class="badge alt"></span><span class="badge"></span><span class="badge"></span><span class="badge alt"></span>
    </div>
  </div>
</aside>

<main class="main">
  <div class="toolbar"><span>30 RESULTS FOUND IN MAIN STORE</span><span class="view">VIEW: ▦ ☰</span><span class="sort">SORT BY: Best Match</span></div>
  <div class="grid">
    <div class="card"><div class="product-img" role="img" aria-label="Belly butter jar product photo"><div class="jar"></div></div><div class="title">BRAMBLE ORGANICS - 30 DAY BELLY BUTTER</div><div class="price"><div><div class="buy">BUY IT <b>NOW</b></div><div class="meta">Postage</div><div class="meta">Time Left</div></div><div style="text-align:right"><div class="old">$19.99</div><div class="now">$14.99</div><div class="meta">3d 12h</div></div></div><span class="btn">VIEW DETAILS</span></div>
    <div class="card"><div class="product-img" role="img" aria-label="Milk enhancer bottle product photo"><div class="bottle"></div></div><div class="title">SUNNYLEAF - NATURAL BREAST MILK ENHANCER</div><div class="price"><div><div class="buy">BUY IT <b>NOW</b></div><div class="meta">Postage</div><div class="meta">Time Left</div></div><div style="text-align:right"><div class="old">$24.99</div><div class="now">$18.99</div><div class="meta">5d 02h</div></div></div><span class="btn">VIEW DETAILS</span></div>
    <div class="card"><div class="product-img" role="img" aria-label="Body wash bottle product photo"><div class="wash"></div></div><div class="title">BRAMBLE ORGANICS - NEWBORN CREME NATURAL BODY WASH</div><div class="price"><div><div class="buy">BUY IT <b>NOW</b></div><div class="meta">Postage</div><div class="meta">Time Left</div></div><div style="text-align:right"><div class="old">$16.99</div><div class="now">$12.99</div><div class="meta">1d 08h</div></div></div><span class="btn">VIEW DETAILS</span></div>

    <div class="card"><div class="product-img" role="img" aria-label="Belly butter jar product photo"><div class="jar"></div></div><div class="title">BRAMBLE ORGANICS - 30 DAY BELLY BUTTER</div><div class="price"><div><div class="buy">BUY IT <b>NOW</b></div><div class="meta">Postage</div><div class="meta">Time Left</div></div><div style="text-align:right"><div class="old">$19.99</div><div class="now">$14.99</div><div class="meta">3d 12h</div></div></div><span class="btn">VIEW DETAILS</span></div>
    <div class="card"><div class="product-img" role="img" aria-label="Milk enhancer bottle product photo"><div class="bottle"></div></div><div class="title">SUNNYLEAF - NATURAL BREAST MILK ENHANCER</div><div class="price"><div><div class="buy">BUY IT <b>NOW</b></div><div class="meta">Postage</div><div class="meta">Time Left</div></div><div style="text-align:right"><div class="old">$24.99</div><div class="now">$18.99</div><div class="meta">5d 02h</div></div></div><span class="btn">VIEW DETAILS</span></div>
    <div class="card"><div class="product-img" role="img" aria-label="Body wash bottle product photo"><div class="wash"></div></div><div class="title">BRAMBLE ORGANICS - NEWBORN CREME NATURAL BODY WASH</div><div class="price"><div><div class="buy">BUY IT <b>NOW</b></div><div class="meta">Postage</div><div class="meta">Time Left</div></div><div style="text-align:right"><div class="old">$16.99</div><div class="now">$12.99</div><div class="meta">1d 08h</div></div></div><span class="btn">VIEW DETAILS</span></div>

    <div class="card"><div class="product-img" role="img" aria-label="Belly butter jar product photo"><div class="jar"></div></div><div class="title">BRAMBLE ORGANICS - 30 DAY BELLY BUTTER</div><div class="price"><div><div class="buy">BUY IT <b>NOW</b></div><div class="meta">Postage</div><div class="meta">Time Left</div></div><div style="text-align:right"><div class="old">$19.99</div><div class="now">$14.99</div><div class="meta">3d 12h</div></div></div><span class="btn">VIEW DETAILS</span></div>
    <div class="card"><div class="product-img" role="img" aria-label="Milk enhancer bottle product photo"><div class="bottle"></div></div><div class="title">SUNNYLEAF - NATURAL BREAST MILK ENHANCER</div><div class="price"><div><div class="buy">BUY IT <b>NOW</b></div><div class="meta">Postage</div><div class="meta">Time Left</div></div><div style="text-align:right"><div class="old">$24.99</div><div class="now">$18.99</div><div class="meta">5d 02h</div></div></div><span class="btn">VIEW DETAILS</span></div>
    <div class="card"><div class="product-img" role="img" aria-label="Body wash bottle product photo"><div class="wash"></div></div><div class="title">BRAMBLE ORGANICS - NEWBORN CREME NATURAL BODY WASH</div><div class="price"><div><div class="buy">BUY IT <b>NOW</b></div><div class="meta">Postage</div><div class="meta">Time Left</div></div><div style="text-align:right"><div class="old">$16.99</div><div class="now">$12.99</div><div class="meta">1d 08h</div></div></div><span class="btn">VIEW DETAILS</span></div>

    <div class="card"><div class="product-img" role="img" aria-label="Belly butter jar product photo"><div class="jar"></div></div><div class="title">BRAMBLE ORGANICS - 30 DAY BELLY BUTTER</div><div class="price"><div><div class="buy">BUY IT <b>NOW</b></div><div class="meta">Postage</div><div class="meta">Time Left</div></div><div style="text-align:right"><div class="old">$19.99</div><div class="now">$14.99</div><div class="meta">3d 12h</div></div></div><span class="btn">VIEW DETAILS</span></div>
    <div class="card"><div class="product-img" role="img" aria-label="Milk enhancer bottle product photo"><div class="bottle"></div></div><div class="title">SUNNYLEAF - NATURAL BREAST MILK ENHANCER</div><div class="price"><div><div class="buy">BUY IT <b>NOW</b></div><div class="meta">Postage</div><div class="meta">Time Left</div></div><div style="text-align:right"><div class="old">$24.99</div><div class="now">$18.99</div><div class="meta">5d 02h</div></div></div><span class="btn">VIEW DETAILS</span></div>
    <div class="card"><div class="product-img" role="img" aria-label="Body wash bottle product photo"><div class="wash"></div></div><div class="title">BRAMBLE ORGANICS - NEWBORN CREME NATURAL BODY WASH</div><div class="price"><div><div class="buy">BUY IT <b>NOW</b></div><div class="meta">Postage</div><div class="meta">Time Left</div></div><div style="text-align:right"><div class="old">$16.99</div><div class="now">$12.99</div><div class="meta">1d 08h</div></div></div><span class="btn">VIEW DETAILS</span></div>

    <div class="card"><div class="product-img" role="img" aria-label="Belly butter jar product photo"><div class="jar"></div></div><div class="title">BRAMBLE ORGANICS - 30 DAY BELLY BUTTER</div><div class="price"><div><div class="buy">BUY IT <b>NOW</b></div><div class="meta">Postage</div><div class="meta">Time Left</div></div><div style="text-align:right"><div class="old">$19.99</div><div class="now">$14.99</div><div class="meta">3d 12h</div></div></div><span class="btn">VIEW DETAILS</span></div>
    <div class="card"><div class="product-img" role="img" aria-label="Milk enhancer bottle product photo"><div class="bottle"></div></div><div class="title">SUNNYLEAF - NATURAL BREAST MILK ENHANCER</div><div class="price"><div><div class="buy">BUY IT <b>NOW</b></div><div class="meta">Postage</div><div class="meta">Time Left</div></div><div style="text-align:right"><div class="old">$24.99</div><div class="now">$18.99</div><div class="meta">5d 02h</div></div></div><span class="btn">VIEW DETAILS</span></div>
    <div class="card"><div class="product-img" role="img" aria-label="Body wash bottle product photo"><div class="wash"></div></div><div class="title">BRAMBLE ORGANICS - NEWBORN CREME NATURAL BODY WASH</div><div class="price"><div><div class="buy">BUY IT <b>NOW</b></div><div class="meta">Postage</div><div class="meta">Time Left</div></div><div style="text-align:right"><div class="old">$16.99</div><div class="now">$12.99</div><div class="meta">1d 08h</div></div></div><span class="btn">VIEW DETAILS</span></div>
  </div>
</main>

<div class="pager"><span>« PREVIOUS</span><span class="on">1</span><span>2</span><span>3</span><span>4</span><span>5</span><span>NEXT »</span></div>
<footer class="footer">© 2014 Little Bloom – Maternity &amp; Baby Store on Lotzy</footer>
</body>
</html>
```